Tree Service Billboard 20x8 ft

We need a billboard design for a tree service company.
The billboard is 20ft x 8 ft so we need a design that is capable to stretching to those dimensions without loosing quality.
I have attached a series of images.
Image 1- Simply a billboard that I think looks good that I would like you to use for inspiration. I am aiming for the same format only no color in the wording, just black white, or gray. I like the the trees in the background, the logo placed to the left, and wording on the right.
Image 2- Current Logo I would like to the left of the billboard
Image 3- Another format of current logo if needed.
Image 4- A drawn out design template
Image 5- Another drawn out design template

Specific things I am looking for
-The contact number to be the largest thing on the design
-The logo on the design
-Key points to the design to say:
Tree Removal
Tree Trimming
Land Development
Stump Grinding
Storm Response
Insured
Free Bids
-The facebook logo
-The Google Logo

```html
<!DOCTYPE html>
<html lang="en">
<head>
<meta charset="utf-8">
<title>Roe's Tree Service Billboard</title>
<link href="https://fonts.googleapis.com/css2?family=Bebas+Neue&family=Orbitron:wght@700;800&display=swap" rel="stylesheet">
<style>
  :root {
    --page: #ffffff;
    --forest-deep: #12301d;
    --forest-mid: #2f6a34;
    --forest-light: #6c9a3c;
    --band: #13261a;
    --olive: #6b7a25;
    --black: #000000;
    --white: #ffffff;
    --ring-gray: #7a7a7a;
    --mark-fill: #2a2a2a;
  }
  * { margin: 0; padding: 0; box-sizing: border-box; }
  html, body {
    width: 1200px;
    height: 655px;
    overflow: hidden;
    background: var(--page);
  }
  .canvas {
    position: relative;
    width: 1200px;
    height: 655px;
    background: var(--page);
  }
  .billboard {
    position: absolute;
    left: 54px;
    top: 109px;
    width: 1090px;
    height: 436px;
    overflow: hidden;
  }
  .forest-backdrop {
    position: absolute;
    left: 0; top: 0;
    width: 1090px;
    height: 364px;
    background:
      radial-gradient(ellipse at 30% 40%, rgba(140,170,70,0.35), transparent 60%),
      radial-gradient(ellipse at 75% 70%, rgba(20,60,35,0.5), transparent 55%),
      linear-gradient(135deg, var(--forest-light) 0%, var(--forest-mid) 45%, var(--forest-deep) 100%);
  }
  .brand-mark {
    position: absolute;
    left: 150px;
    top: 11px;
    width: 268px;
    height: 268px;
  }
  .brand-name {
    position: absolute;
    left: 46px;
    top: 286px;
    width: 480px;
    text-align: center;
    font-family: "Bebas Neue", "Oswald", sans-serif;
    font-size: 80px;
    line-height: 1;
    color: var(--white);
    letter-spacing: 1px;
    white-space: nowrap;
  }
  .service-list {
    position: absolute;
    left: 599px;
    top: 25px;
    width: 491px;
    list-style: none;
  }
  .service-list li {
    height: 41px;
    margin-bottom: 6.5px;
    padding-right: 46px;
    text-align: right;
    font-family: "Orbitron", "Arial Black", sans-serif;
    font-weight: 800;
    font-size: 27px;
    line-height: 41px;
    letter-spacing: 1.5px;
    text-transform: uppercase;
    white-space: nowrap;
  }
  .service-list .on-black { background: var(--black); color: var(--white); }
  .service-list .on-olive { background: var(--olive); color: var(--black); }
  .contact-band {
    position: absolute;
    left: 0;
    top: 364px;
    width: 1090px;
    height: 72px;
    background: var(--band);
    border-top: 4px solid var(--olive);
  }
  .phone-number {
    position: absolute;
    left: 29px;
    top: 6px;
    font-family: "Orbitron", "Arial Black", sans-serif;
    font-weight: 700;
    font-size: 52px;
    line-height: 60px;
    letter-spacing: 6px;
    color: var(--white);
  }
  .social-links {
    position: absolute;
    right: 84px;
    top: 9px;
    display: flex;
    gap: 27px;
  }
  .social-dot {
    width: 49px;
    height: 49px;
    border-radius: 50%;
    border: 3px solid var(--olive);
  }
</style>
</head>
<body>
<div class="canvas">
  <section class="billboard">
    <div class="forest-backdrop" role="img" aria-label="Aerial photograph of a dense green evergreen forest"></div>

    <svg class="brand-mark" viewBox="0 0 268 268" role="img" aria-label="Company emblem: tree with a climbing arborist inside a ring">
      <circle cx="134" cy="134" r="134" fill="var(--white)"/>
      <circle cx="134" cy="134" r="116" fill="none" stroke="var(--ring-gray)" stroke-width="7"/>
      <circle cx="134" cy="134" r="104" fill="var(--mark-fill)"/>
    </svg>

    <div class="brand-name">ROE'S TREE SERVICE</div>

    <ul class="service-list">
      <li class="on-black">Tree Removal</li>
      <li class="on-olive">Tree Trimming</li>
      <li class="on-black">Land Development</li>
      <li class="on-olive">Stump Grinding</li>
      <li class="on-black">Storm Response</li>
      <li class="on-olive">Insured</li>
      <li class="on-black">Free Bids</li>
    </ul>

    <div class="contact-band">
      <div class="phone-number">417-555-0148</div>
      <div class="social-links">
        <span class="social-dot" aria-label="Social profile"></span>
        <span class="social-dot" aria-label="Reviews profile"></span>
      </div>
    </div>
  </section>
</div>
</body>
</html>
```